Creative/innovative law firm website

A law firm website that immediately looks different from other law firm websites. We like the color scheme (dark background with warm, neutral colors) and simple, organic logos (trees, leaves, etc.) of this website: https://brambleworth.legal/

We'll be offering creative/innovative solutions to complex problems faced by state governments, industries, other law firms, and individuals. We're located in Montana (U.S.A.), and the outdoors is a huge part of our lives and identities.

We will need a home page, an "About Us" page with a separate subpage for each attorney (two attorneys), a blog or "Publications" page, a payment portal (which will integrate with Quillo), and a "Services" page.

```html
<!DOCTYPE html>
<html lang="en">
<head>
<meta charset="utf-8">
<title>Ridgeline &amp; Harrow P.C. — Law Firm Process Experts</title>
<link rel="stylesheet" href="https://fonts.googleapis.com/css2?family=Oswald:wght@400;500;600&family=Poppins:wght@400;500;600&display=swap">
<style>
:root{
  --bg:#1f2020;
  --bg-deep:#181919;
  --panel:#252626;
  --field:#1a1b1b;
  --sage:#8c9e84;
  --sage-dark:#7b8d73;
  --sage-soft:#6f7e69;
  --white:#ffffff;
  --text:#d9d9d6;
  --muted:#a9aaa6;
  --line:#6f756c;
}
*{box-sizing:border-box;margin:0;padding:0}
html,body{width:1200px;height:3929px;overflow:hidden}
body{background:var(--bg);color:var(--text);font-family:"Poppins",sans-serif;position:relative}
.abs{position:absolute}
.heading{font-family:"Oswald",sans-serif;font-weight:500;color:var(--white);text-transform:uppercase;line-height:1;letter-spacing:-1px}
.eyebrow{font-family:"Oswald",sans-serif;font-weight:500;color:var(--white);text-transform:uppercase;font-size:19px;display:flex;align-items:center;gap:12px;white-space:nowrap}
.eyebrow::before{content:"";width:56px;height:1px;background:var(--line)}
.btn{display:inline-flex;align-items:center;justify-content:center;font-family:"Poppins",sans-serif;font-weight:600;font-size:12px;text-transform:uppercase;text-decoration:none;letter-spacing:.2px;white-space:nowrap}
.btn-sage{background:var(--sage);color:var(--white)}
.btn-white{background:var(--white);color:#1c1c1c}
.body-copy{font-size:14px;line-height:22px;color:var(--text)}

/* header + hero */
.hero{left:0;top:0;width:1200px;height:702px;background:linear-gradient(180deg,#2c2a2b 0%,#4a3a38 30%,#3a3231 55%,#242323 100%)}
.hero-photo{inset:0;background:radial-gradient(ellipse at 80% 35%,rgba(120,90,80,.45),transparent 60%),linear-gradient(90deg,rgba(25,24,24,.55),rgba(25,24,24,0) 60%)}
.brand{left:88px;top:40px;display:flex;align-items:center;gap:10px;font-family:"Oswald",sans-serif;font-weight:400;font-size:18px;color:var(--white);text-transform:uppercase;text-decoration:none;white-space:nowrap}
.brand-dot{width:12px;height:12px;border-radius:50%;background:var(--white)}
.main-nav{left:584px;top:50px;display:flex;gap:20px;font-size:12px;font-weight:500;text-transform:uppercase}
.main-nav a{color:var(--white);text-decoration:none;position:relative}
.main-nav a.active{color:var(--sage)}
.main-nav a.active::before{content:"";position:absolute;left:-6px;right:-6px;top:-50px;height:2px;background:var(--sage)}
.nav-cta{left:912px;top:40px;width:198px;height:35px}
.hero-eyebrow{left:88px;top:250px;font-weight:400;font-size:19px}
.hero-eyebrow::before{width:60px}
.hero-title{left:88px;top:286px;font-size:68px;line-height:62px}
.hero-text{left:88px;top:436px;width:400px;color:var(--white)}
.hero-btn{left:88px;top:508px;width:118px;height:34px}
.slider-ticks{left:1108px;top:335px;display:flex;flex-direction:column;gap:12px}
.slider-ticks span{width:2px;height:38px;background:rgba(255,255,255,.55)}
.slider-ticks span.on{background:var(--white)}

/* audience cards */
.audience{left:88px;top:703px;width:1022px;height:233px;display:flex}
.aud-card{width:255.5px;height:233px;background:var(--white);display:flex;flex-direction:column;align-items:center;padding-top:44px;font-family:"Oswald",sans-serif;font-size:20px;color:#2b2b2b;text-transform:uppercase;border-right:1px solid #2b2b2b;position:relative}
.aud-card:last-child{border-right:0}
.aud-card svg{width:72px;height:72px;margin-bottom:18px}
.aud-plus{font-family:"Poppins",sans-serif;font-size:30px;font-weight:300;color:#9a9a9a;margin-top:4px}
.aud-card.featured{background:var(--sage);color:var(--white);margin-top:-38px;height:311px;padding-top:44px;outline:8px solid var(--sage-dark);outline-offset:-8px}
.aud-card.featured p{font-family:"Poppins",sans-serif;font-size:12px;line-height:17px;text-transform:none;text-align:center;width:190px;margin-top:6px}
.aud-card.featured .aud-plus{color:var(--white)}

/* approach */
.decor-mountain{left:630px;top:1480px;width:570px;height:320px;background:radial-gradient(ellipse at 50% 70%,rgba(255,255,255,.05),transparent 65%)}
.approach-frame{left:88px;top:1302px;width:411px;height:376px;border:24px solid var(--sage)}
.photo-team{left:185px;top:1118px;width:329px;height:404px;background:linear-gradient(160deg,#e6e4e1 0%,#b9b3ad 45%,#6a4a35 100%)}
.photo-tablet{left:363px;top:1324px;width:233px;height:285px;background:linear-gradient(160deg,#d3cfc9 0%,#a59a8f 50%,#6e5140 100%);border:3px solid var(--bg)}
.approach-eyebrow{left:688px;top:1202px}
.approach-title{left:688px;top:1236px;font-size:68px}
.approach-text{left:688px;top:1316px;width:426px}
.approach-btn{left:688px;top:1446px;width:117px;height:34px}

/* solutions */
.sol-eyebrow{left:100px;top:1849px}
.sol-title{left:88px;top:1880px;font-size:68px}
.sol-text{left:88px;top:1958px;width:436px}
.sol-list{left:88px;top:2046px;list-style:none;font-size:14px;line-height:26.5px;color:var(--text)}
.sol-list li{display:flex;align-items:center;gap:8px}
.sol-list li::before{content:"";width:8px;height:8px;border-radius:50%;background:var(--sage)}
.sol-btn{left:88px;top:2175px;width:118px;height:35px}
.accent-block{left:901px;top:2100px;width:299px;height:264px;background:var(--sage-soft)}
.photo-columns{left:593px;top:1786px;width:517px;height:489px;background:linear-gradient(135deg,#2b2317 0%,#5b4628 40%,#9a7a44 65%,#3a2e1c 100%)}
.decor-justice{left:0;top:2210px;width:460px;height:300px;background:radial-gradient(ellipse at 40% 50%,rgba(255,255,255,.05),transparent 65%)}

/* publications */
.pub-title{left:0;top:2414px;width:1200px;text-align:center;font-size:46px}
.pub-grid{left:168px;top:2501px;display:flex;gap:15px}
.pub-card{width:279px;height:378px;background:var(--panel)}
.pub-img{height:209px}
.pub-img.pen{background:linear-gradient(135deg,#d7d2c7,#8f897f 60%,#3a3937)}
.pub-img.capitol{background:linear-gradient(180deg,#b8bcc1 0%,#8d8f8f 55%,#4e4f4c 100%)}
.pub-img.portrait{background:linear-gradient(135deg,#5a3424,#8a5a3e 50%,#2e2522)}
.pub-body{padding:22px 25px}
.pub-meta{font-size:11px;color:var(--white);display:flex;gap:8px}
.pub-meta span+span::before{content:"•";margin-right:8px}
.pub-head{font-family:"Oswald",sans-serif;font-weight:400;font-size:17px;color:var(--white);text-transform:uppercase;margin:14px 0 10px}
.pub-excerpt{font-size:12px;line-height:18px;color:var(--muted)}

/* contact */
.contact-title{left:0;top:2978px;width:1200px;text-align:center;font-size:46px}
.field-label{font-family:"Oswald",sans-serif;font-weight:500;font-size:13px;color:var(--white);text-transform:uppercase}
.field{background:var(--field);height:46px;width:264px;font-size:12px;color:var(--muted);padding:15px 21px}
.field.message{width:540px;height:141px}
.submit{left:348px;top:3450px;width:117px;height:35px}
.decor-map{left:900px;top:3150px;width:170px;height:95px;background:radial-gradient(ellipse,rgba(255,255,255,.12),transparent 70%)}
.info{left:753px;display:flex;gap:17px}
.info-icon{width:49px;height:49px;background:var(--sage);display:flex;align-items:center;justify-content:center;flex:none}
.info-icon svg{width:22px;height:22px}
.info-label{font-family:"Oswald",sans-serif;font-weight:500;font-size:13px;color:var(--white);text-transform:uppercase}
.info-value{font-size:15px;line-height:18px;color:var(--muted);margin-top:3px;white-space:nowrap}
.photo-gavel{left:941px;top:3279px;width:259px;height:244px;background:radial-gradient(ellipse at 55% 60%,#9a6d2c 0%,#5a3e1c 40%,transparent 72%)}

/* footer */
.footer{left:0;top:3523px;width:1200px;height:406px;background:var(--bg-deep);clip-path:polygon(0 78px,1200px 0,1200px 406px,0 406px)}
.footer-brand{left:0;top:3665px;width:1200px;justify-content:center}
.footer-nav{left:0;top:3733px;width:1200px;display:flex;justify-content:center;gap:22px;font-size:14px;text-transform:uppercase}
.footer-nav a{color:var(--muted);text-decoration:none}
.social{left:0;top:3773px;width:1200px;display:flex;justify-content:center;gap:8px}
.social span{width:34px;height:34px;border-radius:50%;background:#2d2e2e;display:block}
.copyright{left:0;top:3884px;width:1200px;text-align:center;font-family:"Oswald",sans-serif;font-size:13px;color:var(--white);text-transform:uppercase}
.to-top{left:1084px;top:3832px;width:52px;height:49px;background:var(--sage);display:flex;align-items:center;justify-content:center}
</style>
</head>
<body>

<!-- hero -->
<section class="hero abs">
  <div class="hero-photo abs" role="img" aria-label="City skyline at dusk with a busy riverside highway"></div>
</section>
<a class="brand abs"><span class="brand-dot"></span>Ridgeline &amp; Harrow P.C.</a>
<nav class="main-nav abs">
  <a class="active">Home</a><a>Services</a><a>About Us</a><a>Publications</a>
</nav>
<a class="btn btn-sage nav-cta abs">Consultation Request</a>
<p class="eyebrow hero-eyebrow abs">The Law Firm Process Experts</p>
<h1 class="heading hero-title abs">We're located in<br>Montana USA</h1>
<p class="body-copy hero-text abs" style="font-size:15px">Proin gravida nibh vel velit auctor aliquet quis bibendum auctor nisi elit...</p>
<a class="btn btn-white hero-btn abs">Get Started</a>
<div class="slider-ticks abs"><span></span><span></span><span class="on"></span></div>

<!-- audiences -->
<div class="audience abs">
  <div class="aud-card">
    <svg viewBox="0 0 72 72" fill="none" stroke="#2b2b2b" stroke-width="2"><path d="M8 30h56L36 14z"/><path d="M12 34v22M22 34v22M50 34v22M60 34v22"/><rect x="30" y="36" width="12" height="20"/><path d="M6 60h60M36 14V4h8v5h-8"/></svg>
    Governments<span class="aud-plus">+</span>
  </div>
  <div class="aud-card featured">
    <svg viewBox="0 0 72 72" fill="none" stroke="#fff" stroke-width="2"><path d="M6 64V34l14-8v8l14-8v8l14-8V8h8v8h8v48z"/><path d="M14 42h6v6h-6zM28 42h6v6h-6zM42 42h6v6h-6z"/></svg>
    Industries
    <p>Proin gravida nibh vel velit auctor aliquet bibendum auctor nisi elit...</p>
    <span class="aud-plus">+</span>
  </div>
  <div class="aud-card">
    <svg viewBox="0 0 72 72" fill="none" stroke="#2b2b2b" stroke-width="2"><path d="M36 8v54M22 62h28M12 18h48"/><path d="M12 18L4 40h16zM60 18l-8 22h16z"/><path d="M4 40a8 5 0 0016 0M52 40a8 5 0 0016 0"/></svg>
    Other Law Firms<span class="aud-plus">+</span>
  </div>
  <div class="aud-card">
    <svg viewBox="0 0 72 72" fill="none" stroke="#2b2b2b" stroke-width="2"><circle cx="16" cy="16" r="7"/><circle cx="56" cy="16" r="7"/><circle cx="36" cy="16" r="7" fill="#8c9e84"/><path d="M6 46V32a6 6 0 016-6h8M66 46V32a6 6 0 00-6-6h-8M26 62V34a6 6 0 016-6h8a6 6 0 016 6v28"/></svg>
    Individuals<span class="aud-plus">+</span>
  </div>
</div>

<!-- approach -->
<div class="decor-mountain abs" role="img" aria-label="Faint sketched mountain peak"></div>
<div class="approach-frame abs"></div>
<div class="photo-team abs" role="img" aria-label="Two colleagues reviewing work together in a bright office"></div>
<div class="photo-tablet abs" role="img" aria-label="Two colleagues looking at a tablet"></div>
<p class="eyebrow approach-eyebrow abs">Our Holistic</p>
<h2 class="heading approach-title abs">Approach</h2>
<p class="body-copy approach-text abs">Aenean sollicitudin lorem quis bibendum auctor, nisi elit consequat ipsum, nec sagittis sem nibh id elit duis sed odio sit amet nibh vulputate cursus a sit amet mauris morbi accumsan ipsum velit nam tellus a odio tincidunt auctor a ornare odio sed non &nbsp;mauris vitae...</p>
<a class="btn btn-sage approach-btn abs">Learn More</a>

<!-- solutions -->
<p class="eyebrow sol-eyebrow abs">Solutions We Offer</p>
<h2 class="heading sol-title abs">Montana</h2>
<p class="body-copy sol-text abs">Aenean sollicitudin lorem quis bibendum auctor, nisi elit consequat ipsum, nec sagittis sem nibh id elit duis sed odio sit amet nibh vulputate cursus a sit...</p>
<ul class="sol-list abs"><li>State governments</li><li>Industries</li><li>Other law firms</li><li>individuals</li></ul>
<a class="btn btn-sage sol-btn abs">Learn More</a>
<div class="accent-block abs" role="img" aria-label="Decorative sage accent panel"></div>
<div class="photo-columns abs" role="img" aria-label="Classical stone columns beneath a coffered ceiling and skylight"></div>
<div class="decor-justice abs" role="img" aria-label="Faint line drawing of Lady Justice holding scales"></div>

<!-- publications -->
<h2 class="heading pub-title abs">Publications</h2>
<div class="pub-grid abs">
  <article class="pub-card">
    <div class="pub-img pen" role="img" aria-label="Fountain pen writing on lined paper"></div>
    <div class="pub-body"><p class="pub-meta"><span>byJohn</span><span>January 2021</span></p><h3 class="pub-head">Some Blog Heading Here</h3><p class="pub-excerpt">Aenean sollicitudin lorem quis bibendum auctor, consequat elit ipsum nec sagittis sem...</p></div>
  </article>
  <article class="pub-card">
    <div class="pub-img capitol" role="img" aria-label="Domed capitol building under a cloudy sky"></div>
    <div class="pub-body"><p class="pub-meta"><span>byJohn</span><span>January 2021</span></p><h3 class="pub-head">Some Blog Heading Here</h3><p class="pub-excerpt">Aenean sollicitudin lorem quis bibendum auctor, consequat elit ipsum nec sagittis sem...</p></div>
  </article>
  <article class="pub-card">
    <div class="pub-img portrait" role="img" aria-label="Smiling professional woman holding glasses"></div>
    <div class="pub-body"><p class="pub-meta"><span>byJohn</span><span>January 2021</span></p><h3 class="pub-head">Some Blog Heading Here</h3><p class="pub-excerpt">Aenean sollicitudin lorem quis bibendum auctor, consequat elit ipsum nec sagittis sem...</p></div>
  </article>
</div>

<!-- contact -->
<h2 class="heading contact-title abs">Contact Us Today</h2>
<label class="field-label abs" style="left:136px;top:3078px">Name*</label>
<div class="field abs" style="left:136px;top:3105px">Enter your name</div>
<label class="field-label abs" style="left:408px;top:3078px">Email*</label>
<div class="field abs" style="left:408px;top:3105px">Enter your email</div>
<label class="field-label abs" style="left:136px;top:3166px">Phone*</label>
<div class="field abs" style="left:136px;top:3193px">Enter your phone</div>
<label class="field-label abs" style="left:408px;top:3166px">Postal Code*</label>
<div class="field abs" style="left:408px;top:3193px">Enter your postal code</div>
<label class="field-label abs" style="left:136px;top:3254px">Message*</label>
<div class="field message abs" style="left:136px;top:3279px">Type your text</div>
<a class="btn btn-sage submit abs">Submit Now</a>

<div class="decor-map abs" role="img" aria-label="Dotted world map"></div>
<div class="info abs" style="top:3103px">
  <div class="info-icon"><svg viewBox="0 0 24 24" fill="#fff"><path d="M12 2a7 7 0 00-7 7c0 5 7 13 7 13s7-8 7-13a7 7 0 00-7-7zm0 9.5A2.5 2.5 0 1112 6.5a2.5 2.5 0 010 5z"/></svg></div>
  <div><p class="info-label">Location*</p><p class="info-value">Some address line goes here<br>city name country</p></div>
</div>
<div class="info abs" style="top:3190px">
  <div class="info-icon"><svg viewBox="0 0 24 24" fill="#fff"><path d="M6.6 10.8a15 15 0 006.6 6.6l2.2-2.2a1 1 0 011-.25 11.4 11.4 0 003.6.6 1 1 0 011 1V20a1 1 0 01-1 1A17 17 0 013 4a1 1 0 011-1h3.5a1 1 0 011 1 11.4 11.4 0 00.6 3.6 1 1 0 01-.25 1z"/></svg></div>
  <div><p class="info-label">Call Us*</p><p class="info-value">+1 406 555 0182</p></div>
</div>
<div class="info abs" style="top:3264px">
  <div class="info-icon"><svg viewBox="0 0 24 24" fill="#fff"><path d="M2 6l10 7 10-7v12H2z"/><path d="M2 5h20l-10 7z"/></svg></div>
  <div><p class="info-label">Email Us*</p><p class="info-value">hello@ridgelineharrow.legal</p></div>
</div>
<div class="photo-gavel abs" role="img" aria-label="Wooden gavel on law books beside brass scales"></div>

<!-- footer -->
<footer class="footer abs"></footer>
<a class="brand footer-brand abs"><span class="brand-dot"></span>Ridgeline &amp; Harrow P.C.</a>
<nav class="footer-nav abs"><a>Home</a><a>Services</a><a>About Us</a><a>Publications</a><a>Consultation Request</a></nav>
<div class="social abs"><span aria-label="Social profile"></span><span aria-label="Social profile"></span><span aria-label="Social profile"></span><span aria-label="Social profile"></span></div>
<a class="to-top abs" aria-label="Back to top"><svg width="16" height="20" viewBox="0 0 16 20" fill="none" stroke="#fff" stroke-width="1.5"><path d="M8 19V2M2 8l6-6 6 6"/></svg></a>
<p class="copyright abs">Copyright © 2021 Montana USA. All Rights Reserved</p>

</body>
</html>
```